Tarjetas de visita para empresa de aluminio

Empresa con mas de 40 años vendiendo perfiles de aluminio.
Somos fábrica y almacén, queremos renovar la tarjeta de presentación de nuestros comerciales dando una imgen innovadora y tecnógica mezclado con la calidez del respeto al medio ambiente.
Añado el logo de la empresa y actual cara trasera de la tarjeta de visita, el logo es el simbolo WM y la marca TRAVENIC EXTRUSION, la frase 2extrusion y lacado de aluminio" debe cambiarse por "Diseño, extrusión, lacado, anodizado y mecanizado de precisión de aluminio" o en su defecto incluir todos esos servicios que hacemos o una frase mas pegadiza.

We are an aluminium factory, we produce and stock profiles of aluminium.
we want to renew visit card of our sellers, we are looking for something that show innovation, tecnology and environment respect.
Upload our actual logo and back of visit card, logo WM and brand TRAVENIC EXTRUSION must be keept.
Text "Extrusion y lacado de aluminio" must be changed for "Diseño, extrusion, lacado, anodizado y mecanizado de precisión de aluminio" or something like that

```html
<!DOCTYPE html>
<html lang="es">
<head>
<meta charset="utf-8">
<title>Tarjetas de visita – Travenic Extrusion</title>
<link rel="stylesheet" href="https://fonts.googleapis.com/css2?family=Poppins:wght@500;600;700&family=Old+Standard+TT&display=swap">
<style>
  :root {
    --stage-grey: #8b8987;
    --page-white: #ffffff;
    --gold-light: #f6d88c;
    --gold-mid: #f0b648;
    --gold-deep: #e9962e;
    --silver-light: #f4f4f4;
    --silver-dark: #8d8d8d;
    --ink: #2a2320;
    --brand-ink: #3b3835;
    --accent: #e8703a;
  }
  * { margin: 0; padding: 0; box-sizing: border-box; }
  html, body { width: 1200px; height: 2643px; overflow: hidden; }
  body { position: relative; background: var(--page-white); font-family: "Poppins", sans-serif; color: var(--ink); }

  .stage { position: absolute; left: 0; top: 0; width: 1200px; height: 900px; background: var(--stage-grey); }

  .card {
    position: absolute; width: 420px; height: 735px; overflow: hidden;
    background:
      radial-gradient(ellipse 60% 22% at 50% 22%, rgba(255,246,214,.75), transparent 70%),
      linear-gradient(90deg, rgba(233,150,46,.35), transparent 25%, rgba(255,240,200,.35) 50%, transparent 75%, rgba(233,150,46,.35)),
      linear-gradient(180deg, var(--gold-mid) 0%, var(--gold-light) 22%, var(--gold-mid) 50%, #f3c064 72%, var(--gold-deep) 100%);
    box-shadow: 0 6px 14px rgba(0,0,0,.18);
    transform-origin: 0 0;
  }
  .card.is-mini { transform: scale(.738); }
  .card::before, .card::after {
    content: ""; position: absolute; left: 0; right: 0; height: 12px;
    background: linear-gradient(90deg, var(--silver-dark), var(--silver-light) 30%, #bdbdbd 55%, var(--silver-light) 80%, var(--silver-dark));
  }
  .card::before { top: 0; }
  .card::after { bottom: 0; }

  .brand { position: absolute; left: 0; right: 0; text-align: center; }
  .brand-mark { display: block; margin: 0 auto 12px; width: 150px; height: 92px; border-radius: 50%; border: 4px solid #9a9a9a; }
  .brand-name { font-weight: 500; color: var(--brand-ink); letter-spacing: .04em; }
  .tagline { font-weight: 600; text-transform: uppercase; line-height: 1.25; color: var(--ink); }

  .front .brand { top: 245px; }
  .front .brand-name { font-size: 27px; }
  .front .tagline { font-size: 17.5px; margin-top: 18px; }

  .back .brand { top: 52px; }
  .back .brand-mark { width: 125px; height: 72px; margin-bottom: 10px; border-width: 3px; }
  .back .brand-name { font-size: 21px; }
  .back .tagline { font-size: 14.5px; margin-top: 12px; line-height: 1.22; }

  .person { position: absolute; top: 258px; left: 0; right: 0; text-align: center; font-family: "Old Standard TT", serif; }
  .person-name { font-size: 23px; }
  .person-role { font-size: 22px; }

  .contacts { position: absolute; top: 362px; left: 70px; right: 20px; list-style: none; }
  .contact { display: flex; align-items: flex-start; gap: 12px; }
  .contact + .contact { margin-top: 8px; }
  .icon { flex: none; width: 30px; height: 30px; border-radius: 50%; background: var(--accent); display: flex; align-items: center; justify-content: center; }
  .icon svg { width: 16px; height: 16px; fill: none; stroke: #fff; stroke-width: 2; stroke-linecap: round; stroke-linejoin: round; }
  .label { display: block; font-family: "Old Standard TT", serif; font-size: 14px; line-height: 1; }
  .value { display: block; font-weight: 600; font-size: 15.5px; line-height: 1.25; }
  .address .value { font-size: 14.5px; }
  .address .value + .value { margin-top: 6px; }
  .web .value { font-size: 16px; letter-spacing: .06em; padding-top: 4px; }
</style>
</head>
<body>

<section class="stage">
  <article class="card front is-mini" style="left:247px; top:193px;">
    <div class="brand">
      <span class="brand-mark"></span>
      <p class="brand-name">TRAVENIC EXTRUSION</p>
      <p class="tagline">Diseño, extrusion, lacado,<br>anodizado y mecanizado de<br>precisión de aluminio</p>
    </div>
  </article>

  <article class="card back is-mini" style="left:643px; top:165px;">
    <div class="brand">
      <span class="brand-mark"></span>
      <p class="brand-name">TRAVENIC EXTRUSION</p>
      <p class="tagline">Diseño, extrusion, lacado,<br>anodizado y mecanizado de<br>precisión de aluminio</p>
    </div>
    <div class="person"><p class="person-name">MARCOS HERRERA LIDÓN</p><p class="person-role">Comercial</p></div>
    <ul class="contacts">
      <li class="contact address"><span class="icon"><svg viewBox="0 0 16 16"><path d="M8 15s5-5 5-8.5a5 5 0 0 0-10 0C3 10 8 15 8 15z"/><circle cx="8" cy="6.5" r="1.8"/></svg></span><div><span class="value">POL. IND. LOS ÁLAMOS - C/ 4 Nº 22</span><span class="value">41820 VILLANUEVA DEL RÍO<br>(SEVILLA) APARTADO DE<br>CORREOS 305 B</span></div></li>
      <li class="contact"><span class="icon"><svg viewBox="0 0 16 16"><rect x="2" y="4" width="12" height="8.5" rx="1"/><path d="M2.5 4.5 8 9l5.5-4.5"/></svg></span><div><span class="label">E-mail:</span><span class="value">marcosherrera@travenic.com</span></div></li>
      <li class="contact"><span class="icon"><svg viewBox="0 0 16 16"><path d="M4 2.5h2.2l1 3-1.5 1a7 7 0 0 0 3.8 3.8l1-1.5 3 1V12a1.5 1.5 0 0 1-1.5 1.5A10 10 0 0 1 2.5 4 1.5 1.5 0 0 1 4 2.5z"/></svg></span><div><span class="label">Movil:</span><span class="value">600 12 34 56</span></div></li>
      <li class="contact"><span class="icon"><svg viewBox="0 0 16 16"><path d="M4 2.5h2.2l1 3-1.5 1a7 7 0 0 0 3.8 3.8l1-1.5 3 1V12a1.5 1.5 0 0 1-1.5 1.5A10 10 0 0 1 2.5 4 1.5 1.5 0 0 1 4 2.5z"/></svg></span><div><span class="label">Telf:</span><span class="value">955 00 11 22</span></div></li>
      <li class="contact"><span class="icon"><svg viewBox="0 0 16 16"><path d="M4.5 6V2.5h7V6"/><rect x="2.5" y="6" width="11" height="5" rx="1"/><rect x="4.5" y="9.5" width="7" height="4"/></svg></span><div><span class="label">Fax:</span><span class="value">955 00 33 44</span></div></li>
      <li class="contact web"><span class="icon"><svg viewBox="0 0 16 16"><circle cx="8" cy="8" r="5.5"/><path d="M2.5 8h11M8 2.5c-2 2-2 9 0 11M8 2.5c2 2 2 9 0 11"/></svg></span><div><span class="value">www.travenic.com</span></div></li>
    </ul>
  </article>
</section>

<article class="card front" style="left:390px; top:1005px;">
  <div class="brand">
    <span class="brand-mark"></span>
    <p class="brand-name">TRAVENIC EXTRUSION</p>
    <p class="tagline">Diseño, extrusion, lacado,<br>anodizado y mecanizado de<br>precisión de aluminio</p>
  </div>
</article>

<article class="card back" style="left:390px; top:1820px;">
  <div class="brand">
    <span class="brand-mark"></span>
    <p class="brand-name">TRAVENIC EXTRUSION</p>
    <p class="tagline">Diseño, extrusion, lacado,<br>anodizado y mecanizado de<br>precisión de aluminio</p>
  </div>
  <div class="person"><p class="person-name">MARCOS HERRERA LIDÓN</p><p class="person-role">Comercial</p></div>
  <ul class="contacts">
    <li class="contact address"><span class="icon"><svg viewBox="0 0 16 16"><path d="M8 15s5-5 5-8.5a5 5 0 0 0-10 0C3 10 8 15 8 15z"/><circle cx="8" cy="6.5" r="1.8"/></svg></span><div><span class="value">POL. IND. LOS ÁLAMOS - C/ 4 Nº 22</span><span class="value">41820 VILLANUEVA DEL RÍO<br>(SEVILLA) APARTADO DE<br>CORREOS 305 B</span></div></li>
    <li class="contact"><span class="icon"><svg viewBox="0 0 16 16"><rect x="2" y="4" width="12" height="8.5" rx="1"/><path d="M2.5 4.5 8 9l5.5-4.5"/></svg></span><div><span class="label">E-mail:</span><span class="value">marcosherrera@travenic.com</span></div></li>
    <li class="contact"><span class="icon"><svg viewBox="0 0 16 16"><path d="M4 2.5h2.2l1 3-1.5 1a7 7 0 0 0 3.8 3.8l1-1.5 3 1V12a1.5 1.5 0 0 1-1.5 1.5A10 10 0 0 1 2.5 4 1.5 1.5 0 0 1 4 2.5z"/></svg></span><div><span class="label">Movil:</span><span class="value">600 12 34 56</span></div></li>
    <li class="contact"><span class="icon"><svg viewBox="0 0 16 16"><path d="M4 2.5h2.2l1 3-1.5 1a7 7 0 0 0 3.8 3.8l1-1.5 3 1V12a1.5 1.5 0 0 1-1.5 1.5A10 10 0 0 1 2.5 4 1.5 1.5 0 0 1 4 2.5z"/></svg></span><div><span class="label">Telf:</span><span class="value">955 00 11 22</span></div></li>
    <li class="contact"><span class="icon"><svg viewBox="0 0 16 16"><path d="M4.5 6V2.5h7V6"/><rect x="2.5" y="6" width="11" height="5" rx="1"/><rect x="4.5" y="9.5" width="7" height="4"/></svg></span><div><span class="label">Fax:</span><span class="value">955 00 33 44</span></div></li>
    <li class="contact web"><span class="icon"><svg viewBox="0 0 16 16"><circle cx="8" cy="8" r="5.5"/><path d="M2.5 8h11M8 2.5c-2 2-2 9 0 11M8 2.5c2 2 2 9 0 11"/></svg></span><div><span class="value">www.travenic.com</span></div></li>
  </ul>
</article>

</body>
</html>
```